Upscale business cards needed for Board of Directors

We need professional business cards created for members of our family business Board of Directors. We would like these relatively simple and straightforward, but also with a unique element to set them apart. Probably stick with neutral and simple colors - white, grey etc. We need space for the traditional elements, including name, title, address, email/phone number. And we will be creating several from this template so it needs to be template that is easy to switch information in and out of.
Business
See description

```html
<!DOCTYPE html>
<html lang="en">
<head>
<meta charset="utf-8">
<title>Harbourline Group – Board Business Card</title>
<link href="https://fonts.googleapis.com/css2?family=Open+Sans:ital,wght@0,400;0,700;1,700&display=swap" rel="stylesheet">
<style>
  :root {
    --page: #f3f3f3;
    --card-light: #ffffff;
    --card-dark: #2b2a28;
    --gold: #b9a57a;
    --ink: #262524;
    --text-light: #ffffff;
    --text-soft: #e6e4df;
  }
  * { margin: 0; padding: 0; box-sizing: border-box; }
  html, body {
    width: 1200px; height: 832px; overflow: hidden;
    background: var(--page);
    font-family: "Open Sans", Arial, sans-serif;
  }
  .card {
    position: absolute; left: 177px; top: 187px;
    width: 811px; height: 467px;
    background: var(--card-dark);
    overflow: hidden;
  }
  .card__brand-panel {
    position: absolute; left: 0; top: 0; width: 336px; height: 413px;
  }
  .card__brand-panel svg { position: absolute; left: 0; top: 0; }
  .brand-name {
    position: absolute; left: 0; top: 206px; width: 336px;
    text-align: center; color: var(--ink);
    font-size: 27px; font-weight: 700; line-height: 1;
  }
  .person {
    position: absolute; left: 336px; width: 475px; top: 86px;
    text-align: center; color: var(--text-light);
  }
  .person__name { font-size: 24px; font-weight: 700; letter-spacing: 0.3px; line-height: 1.3; }
  .person__role { font-size: 21px; font-weight: 400; color: var(--text-soft); line-height: 1.35; }
  .contacts { position: absolute; left: 393px; top: 171px; list-style: none; }
  .contacts__item {
    display: flex; align-items: center; height: 42px;
    color: var(--text-light); font-size: 25px; font-weight: 400;
  }
  .contacts__icon { width: 22px; height: 24px; margin-right: 15px; flex: none; }
  .card__tagline-band {
    position: absolute; left: 0; bottom: 0; width: 811px; height: 54px;
    background: var(--gold);
    display: flex; align-items: center; justify-content: center;
  }
  .tagline {
    color: var(--text-light); font-size: 23px; font-weight: 700; font-style: italic;
    letter-spacing: 0.3px;
  }
</style>
</head>
<body>
  <div class="card">
    <div class="card__brand-panel">
      <svg width="336" height="413" viewBox="0 0 336 413" aria-hidden="true">
        <polygon points="0,0 274,0 336,100 336,413 0,413" fill="var(--card-light)"/>
        <polygon points="274,0 336,100 274,100" fill="var(--gold)"/>
      </svg>
      <div class="brand-name">Harbourline Group</div>
    </div>

    <div class="person">
      <div class="person__name">NAME SURNAME</div>
      <div class="person__role">Position</div>
    </div>

    <ul class="contacts">
      <li class="contacts__item">
        <svg class="contacts__icon" viewBox="0 0 24 24" aria-hidden="true"><path d="M6.5 2.5l3 4-2 2.2c1.2 2.8 3.2 4.8 6 6l2.2-2 4 3-2 4c-8-.5-14.7-7.2-15.2-15.2z" fill="none" stroke="var(--gold)" stroke-width="2" stroke-linejoin="round"/></svg>
        012 345 67890
      </li>
      <li class="contacts__item">
        <svg class="contacts__icon" viewBox="0 0 24 24" aria-hidden="true"><rect x="5" y="2" width="14" height="20" rx="2" fill="none" stroke="var(--gold)" stroke-width="2"/><line x1="10" y1="18" x2="14" y2="18" stroke="var(--gold)" stroke-width="2"/></svg>
        012 345 67891
      </li>
      <li class="contacts__item">
        <svg class="contacts__icon" viewBox="0 0 24 24" aria-hidden="true"><rect x="2" y="6" width="20" height="13" fill="none" stroke="var(--gold)" stroke-width="2"/><path d="M2 6l10 7 10-7" fill="none" stroke="var(--gold)" stroke-width="2"/></svg>
        info@company.com
      </li>
      <li class="contacts__item">
        <svg class="contacts__icon" viewBox="0 0 24 24" aria-hidden="true"><circle cx="12" cy="12" r="9" fill="none" stroke="var(--gold)" stroke-width="2"/><ellipse cx="12" cy="12" rx="4" ry="9" fill="none" stroke="var(--gold)" stroke-width="1.6"/><line x1="3" y1="12" x2="21" y2="12" stroke="var(--gold)" stroke-width="1.6"/></svg>
        www.company.com
      </li>
      <li class="contacts__item">
        <svg class="contacts__icon" viewBox="0 0 24 24" aria-hidden="true"><path d="M12 23s-7-8.5-7-13.5a7 7 0 0 1 14 0C19 14.5 12 23 12 23z" fill="var(--gold)"/><circle cx="12" cy="9.5" r="2.8" fill="var(--card-dark)"/></svg>
        Address
      </li>
    </ul>

    <div class="card__tagline-band">
      <span class="tagline">YOUR TAGLINE HERE</span>
    </div>
  </div>
</body>
</html>
```